Packaging / Logo Design for Toddler Potty Liners

We need a packaging and logo design for a new company based in Atlanta called "BrimLeaf". We manufacture innovative, eco-friendly baby / toddler products. Our initial product is a flushable, biodegradable potty liner used for toddler potty training. We are looking for a modern / clean / eco-friendly packaging and logo design for this product. Each package will contain 20 liners. Box dimensions are as follows:

Length = 8.5in
Width = 5in
Height = 1.5in

The box will have a perforated top measuring 6.5 inches (see attached pictures). Liners will be folded inside and individually pulled out through the perforated top (similar to a Softora box). See attached pictures of similar box.

Packaging should appeal to parents as an easy to use, eco-friendly, sanitary solution to potty training. This product is an alternative to the conventional way of cleaning / disinfecting the potty after each use, a process that most parents dread!

The closest competitors are NeatPips (www.neatpips-example.com) and Lumbra (www.lumbra-example.com) - you can reference their websites to get an idea for the product and use. However, their liners are not flushable and that is the biggest differentiator of this product. Their packaging seems conventional and non-inspiring so we would like our design to stand out from theirs.

We would like to see creative, modern cardboard box designs which will make our brand stand out from the competition. We would like to use one of the following color schemes: 1) a modern green color on a white background, 2) a modern green color on plain cardboard background, or 3) white on a modern green background. May use one or two additional complementary colors. See attached modern green image for inspiration. We would like to see clean lines, text and illustrations. We are looking forward to seeing any cool ideas you may have!
Updates

Brief has been updated with our desired color schemes and pictures for inspiration.  Please read updated brief before beginning your design!  Thanks so much!

Industry/Entity Type

Biodegradable

Requirements
Must have
• The front of the package should include the following info:

Logo: BrimLeaf
Product Name: Flushable Potty Chair Liners
Clean and Convenient
Fits All Potty Chairs
Sewer and Septic Safe
Patent Pending
20 Single-Use Flushable Potty Chair Liners

Package should also have space for some simple instructions (preferably with illustrations). This can be placed on one of the sides of the box.
1. Place liner over clean, dry (underline the word dry) potty bowl.
2. After your toddler uses the potty, remove liner (do not tie) and flush.
3. Give your toddler a high five!

Please submit design considering all sides of the box!

```html
<!DOCTYPE html>
<html lang="en">
<head>
<meta charset="utf-8">
<title>BrimLeaf Flushable Potty Chair Liners – Packaging</title>
<link rel="stylesheet" href="https://fonts.googleapis.com/css2?family=Itim&display=swap">
<style>
  :root {
    --stage: #d9dbd8;
    --leaf-green: #8cb23a;
    --leaf-green-dark: #7fa532;
    --chalk: #f1f4ea;
    --text-font: "Itim", "Comic Sans MS", sans-serif;
  }
  * { margin: 0; padding: 0; box-sizing: border-box; }
  html, body {
    width: 1200px;
    height: 896px;
    overflow: hidden;
    background: var(--stage);
    font-family: var(--text-font);
    color: var(--chalk);
  }
  .dieline {
    position: absolute;
    left: 60px;
    top: 200px;
    display: flex;
    gap: 16px;
  }
  .panel {
    position: relative;
    height: 494px;
    background: var(--leaf-green);
    overflow: hidden;
  }
  .panel-front { width: 840px; }
  .panel-side {
    width: 160px;
    background: var(--leaf-green-dark);
    display: flex;
    flex-direction: column;
    align-items: center;
    padding: 24px 14px;
    text-align: center;
  }
  .front-lines {
    position: absolute;
    inset: 0;
    width: 100%;
    height: 100%;
  }
  .brand {
    position: absolute;
    display: flex;
    align-items: center;
    gap: 10px;
  }
  .brand-dot {
    border-radius: 50%;
    background: var(--chalk);
  }
  .brand-name { color: var(--chalk); font-weight: 400; }
  .panel-front .brand { left: 46px; top: 92px; }
  .panel-front .brand-dot { width: 22px; height: 22px; }
  .panel-front .brand-name { font-size: 50px; line-height: 1.2; }
  .product-name {
    position: absolute;
    left: 46px;
    top: 180px;
    font-size: 46px;
    line-height: 1.2;
    font-weight: 400;
    letter-spacing: 0.5px;
  }
  .benefits {
    position: absolute;
    left: 430px;
    top: 275px;
    list-style: none;
    font-size: 27px;
    line-height: 31px;
  }
  .benefits li::before { content: "· "; }
  .benefits li:nth-child(1) { padding-left: 50px; }
  .benefits li:nth-child(2) { padding-left: 30px; }
  .benefits li:nth-child(3) { padding-left: 14px; }
  .count-front {
    position: absolute;
    right: 40px;
    bottom: 14px;
    font-size: 40px;
    line-height: 1.2;
  }
  .panel-side .brand { position: static; flex-direction: column; gap: 8px; }
  .panel-side .brand-dot { width: 16px; height: 16px; }
  .panel-side .brand-name { font-size: 28px; }
  .count-side { font-size: 17px; margin: 14px 0 22px; }
  .side-copy {
    font-size: 13px;
    line-height: 1.45;
    text-decoration: underline;
  }
</style>
</head>
<body>
  <main class="dieline">
    <section class="panel panel-front" aria-label="Front panel">
      <svg class="front-lines" viewBox="0 0 840 494" aria-hidden="true">
        <path d="M80 0 C 110 70, 300 110, 480 96 C 620 86, 700 40, 712 0"
              fill="none" stroke="var(--chalk)" stroke-width="2"/>
        <ellipse cx="600" cy="337" rx="240" ry="80"
                 fill="none" stroke="var(--chalk)" stroke-width="4"/>
      </svg>
      <div class="brand">
        <span class="brand-dot"></span>
        <span class="brand-name">BrimLeaf</span>
      </div>
      <h1 class="product-name">Flushable Potty Chair Liners</h1>
      <ul class="benefits">
        <li>Clean and Convenient</li>
        <li>Sewer and Septic Safe</li>
        <li>Fits All Potty Chairs</li>
        <li>Patent Pending</li>
      </ul>
      <p class="count-front">20 Liners</p>
    </section>
    <section class="panel panel-side" aria-label="Side panel">
      <div class="brand">
        <span class="brand-dot"></span>
        <span class="brand-name">BrimLeaf</span>
      </div>
      <p class="count-side">20 Liners</p>
      <p class="side-copy">Soft, flushable liners that make potty training simple. Place a liner over a clean, dry potty bowl. After use, remove the liner without tying it and flush it away. Made from plant-based materials that break down safely in sewer and septic systems.</p>
    </section>
  </main>
</body>
</html>
```